Pemberton Dialworks Business Card Design

Double Sided Business Card Design for a Locksmith company specializing in Safecracking, safe & vault service.

```html
<!DOCTYPE html>
<html lang="en">
<head>
<meta charset="utf-8">
<title>Pemberton Dialworks Business Card</title>
<link rel="stylesheet" href="https://fonts.googleapis.com/css2?family=Noto+Sans:wght@400;700&display=swap">
<style>
  :root {
    --backdrop: #e4e4e4;
    --card-dark: #060708;
    --card-light: #f4f4f4;
    --brand-green: #1f7a3c;
    --ink: #1a1a1a;
    --ink-soft: #dcdcdc;
    --watermark: #e1e7e2;
  }
  * { margin: 0; padding: 0; box-sizing: border-box; }
  html, body {
    width: 1200px; height: 960px; overflow: hidden;
    background: var(--backdrop);
    font-family: "Noto Sans", Arial, sans-serif;
  }
  .card {
    position: absolute; left: 303px; width: 598px; height: 342px; overflow: hidden;
  }
  .card--front { top: 119px; background: var(--card-dark); }
  .card--back { top: 514px; background: var(--card-light); }

  .brand { position: absolute; display: flex; align-items: center; }
  .brand__dot { border-radius: 50%; background: var(--brand-green); flex: none; }
  .brand__name { font-weight: 700; text-transform: uppercase; line-height: 1.02; letter-spacing: 0.5px; }

  .card--front .brand { left: 98px; top: 109px; }
  .card--front .brand__dot { width: 122px; height: 122px; }
  .card--front .brand__name { margin-left: 16px; font-size: 33px; color: #ffffff; }

  .license {
    position: absolute; left: 0; right: 0; top: 294px; text-align: center;
    font-size: 14px; color: var(--ink-soft);
  }

  .card--back .brand { left: 42px; top: 33px; }
  .card--back .brand__dot { width: 73px; height: 73px; }
  .card--back .brand__name { margin-left: 10px; font-size: 21px; color: var(--ink); }

  .person { position: absolute; right: 44px; top: 54px; text-align: right; }
  .person__name { font-size: 19px; font-weight: 700; color: var(--brand-green); }
  .person__role { font-size: 14.5px; color: var(--ink); margin-top: 1px; }

  .watermark {
    position: absolute; left: 338px; top: 122px; width: 270px; height: 270px;
    border-radius: 50%; background: var(--watermark);
  }

  .details { position: absolute; left: 42px; top: 173px; font-size: 14.5px; color: var(--ink); line-height: 20px; }
  .details__company { color: var(--brand-green); }
  .contacts { list-style: none; margin-top: 11px; }
  .contacts li { display: flex; align-items: center; gap: 6px; }
  .contacts svg { width: 13px; height: 13px; fill: var(--brand-green); flex: none; }
</style>
</head>
<body>
  <section class="card card--front">
    <div class="brand">
      <span class="brand__dot"></span>
      <span class="brand__name">Pemberton<br>Dialworks</span>
    </div>
    <p class="license">Texas DPS Locksmith License# B20418736</p>
  </section>

  <section class="card card--back">
    <div class="watermark"></div>
    <div class="brand">
      <span class="brand__dot"></span>
      <span class="brand__name">Pemberton<br>Dialworks</span>
    </div>
    <div class="person">
      <p class="person__name">Graham Ellery</p>
      <p class="person__role">President</p>
    </div>
    <div class="details">
      <p class="details__company">Pemberton Dialworks LLC</p>
      <p>1840 Marlow Park Ave, Suite 210</p>
      <p>Brookvale , TX , 75094</p>
      <ul class="contacts">
        <li>
          <svg viewBox="0 0 16 16" aria-hidden="true"><path d="M3.6 1.2l2.3 2.6-1.4 2.1c.9 2 2.5 3.6 4.5 4.5l2.1-1.4 2.6 2.3-1.3 2.5C7.8 13.4 2.6 8.2 1.1 2.5z"/></svg>
          555-014-2297
        </li>
        <li>
          <svg viewBox="0 0 16 16" aria-hidden="true"><path d="M1 3h14v10H1zm1.5 1.5v.3L8 8.6l5.5-3.8v-.3zm0 2.1v4.9h11V6.6L8 10.4z"/></svg>
          graham@pembertondialworks.com
        </li>
        <li>
          <svg viewBox="0 0 16 16" aria-hidden="true"><path d="M8 1a7 7 0 100 14A7 7 0 008 1zm5.4 6.2h-2.3a11 11 0 00-1-4.3 5.6 5.6 0 013.3 4.3zM8 2.5c.7.9 1.4 2.6 1.6 4.7H6.4C6.6 5.1 7.3 3.4 8 2.5zM5.9 2.9a11 11 0 00-1 4.3H2.6a5.6 5.6 0 013.3-4.3zM2.6 8.8h2.3a11 11 0 001 4.3 5.6 5.6 0 01-3.3-4.3zM8 13.5c-.7-.9-1.4-2.6-1.6-4.7h3.2c-.2 2.1-.9 3.8-1.6 4.7zm2.1-.4a11 11 0 001-4.3h2.3a5.6 5.6 0 01-3.3 4.3z"/></svg>
          www.pembertondialworks.com
        </li>
      </ul>
    </div>
  </section>
</body>
</html>
```